Torvin Electrics Flyer Design Advertising

I am after an A5 Flyer design to help promote my electrical services business.
I would like to have information on what my business offers, photos of electrical work, and specials/deals for an amount of time.

Industry/Entity Type

Electrician

Font styles to use
Sans Serif

Colors
0292cd
33a6d7
85cae6
3176b5
333333
1b1b1b
ffffff
5c5c5c
474747

Requirements
Must have
• Specialising in New homes, renovations and commercial projects
• Contact details:
• ph. 0457 613 948
• email admin@torvinelectrics.com.au
• facebook TorvinElectrics
• Specials/Deals:
• 10% off all electrical services
• or
• Free LED downlights on installation
• *Terms conditions apply
• ALL RESIDENTIAL & COMMERCIAL ELECTRICAL SERVICES
• - New Home installations
• - Commercial projects
• - Shop fit outs
• - Renovations
• - Smoke Detectors
• - Air Conditioning and Ceiling Fans
• - Garden Lighting
• - Oven and Cooktop Installations
• - Power Point installation
• - LED lighting upgrades
• - Security Lighting
• - Switchboard upgrades
• - Test and Tag
• - Commercial Property
• - General Electrical Maintenance

```html
<!DOCTYPE html>
<html lang="en">
<head>
<meta charset="utf-8">
<title>Torvin Electrics Flyer</title>
<link rel="stylesheet" href="https://fonts.googleapis.com/css2?family=Roboto+Condensed:wght@400;700&family=Roboto:wght@400;700&display=swap">
<style>
  :root {
    --blue: #0292cd;
    --blue-mid: #33a6d7;
    --blue-light: #85cae6;
    --blue-deep: #3176b5;
    --ink: #333333;
    --ink-dark: #1b1b1b;
    --white: #ffffff;
    --grey: #5c5c5c;
    --grey-dark: #474747;
    --paper: #e6e6e6;
    --bg: #d9d9d9;
  }
  * { margin: 0; padding: 0; box-sizing: border-box; }
  html, body { width: 1200px; height: 1200px; overflow: hidden; background: var(--bg); }
  .flyer {
    position: absolute; left: 205px; top: 50px; width: 790px; height: 1100px;
    background: var(--white); overflow: hidden;
    font-family: "Roboto Condensed", "Arial Narrow", sans-serif;
    box-shadow: 0 10px 30px rgba(0,0,0,.25);
  }
  .abs { position: absolute; }
  .hero-photo {
    left: 0; top: 0; width: 790px; height: 512px;
    background: linear-gradient(180deg, #d8dadb 0%, #eef0f0 35%, #b9b6ad 70%, #7d725f 100%);
  }
  .web-strip {
    left: 28px; top: 0; width: 44px; height: 450px; background: var(--blue);
    display: flex; align-items: center; justify-content: center;
  }
  .web-strip span {
    transform: rotate(-90deg); white-space: nowrap; color: var(--white);
    font-family: "Roboto", sans-serif; font-size: 19px; letter-spacing: 2px;
  }
  .brand {
    right: 26px; top: 30px; display: flex; align-items: center; gap: 10px;
  }
  .brand-dot { width: 86px; height: 86px; border-radius: 50%; background: var(--grey-dark); }
  .brand-name {
    color: var(--white); font-weight: 700; font-size: 30px; line-height: 1;
    text-transform: uppercase;
  }
  .specialising {
    left: 296px; top: 420px; width: 494px; height: 92px; background: var(--blue);
    color: var(--white); text-transform: uppercase; font-weight: 700;
    padding: 14px 0 0 26px;
  }
  .specialising .lead { font-size: 33px; line-height: 1.05; }
  .specialising .sub { font-size: 22px; line-height: 1.1; }
  .deals-label {
    left: 0; top: 512px; width: 86px; height: 214px; background: var(--grey-dark);
    display: flex; align-items: center; justify-content: center;
  }
  .deals-label span {
    transform: rotate(-90deg); white-space: nowrap; color: var(--white);
    font-weight: 700; font-size: 26px; text-transform: uppercase;
  }
  .deals {
    left: 86px; top: 512px; width: 303px; height: 214px; background: var(--grey);
    color: var(--white); text-align: center; text-transform: uppercase;
    padding-top: 14px;
  }
  .deals .big { font-size: 31px; font-weight: 700; line-height: 1.05; }
  .deals .small { font-size: 19px; line-height: 1.1; }
  .deals .or { font-size: 56px; font-weight: 700; color: var(--blue); line-height: 1.05; }
  .kitchen-photo {
    left: 389px; top: 512px; width: 401px; height: 214px;
    background: linear-gradient(180deg, #f2f1ee 0%, #d7d2c8 45%, #8d7f6c 75%, #c9bfb0 100%);
  }
  .services-title {
    left: 0; top: 726px; width: 294px; height: 200px;
    background: linear-gradient(160deg, var(--blue-mid), var(--blue-deep));
    color: var(--white); font-weight: 700; text-transform: uppercase;
    padding: 50px 0 0 26px; line-height: 1.02;
  }
  .services-title .l1 { font-size: 35px; }
  .services-title .l2 { font-size: 35px; color: var(--ink-dark); }
  .services-title .l3 { font-size: 27px; }
  .services-list {
    left: 294px; top: 726px; width: 496px; height: 200px; background: var(--paper);
    display: flex; padding: 14px 0 0 8px; gap: 8px;
  }
  .services-list ul { list-style: none; }
  .services-list ul:first-child { width: 246px; }
  .services-list li {
    font-family: "Roboto", sans-serif; font-weight: 700; font-size: 13.5px;
    color: var(--ink); line-height: 24px; white-space: nowrap;
  }
  .services-list li::before {
    content: ""; display: inline-block; width: 5px; height: 5px; border-radius: 50%;
    background: var(--blue); margin: 0 6px 2px 0; vertical-align: middle;
  }
  .call {
    left: 0; top: 934px; width: 790px; height: 74px; background: var(--grey-dark);
    color: var(--white); font-weight: 700; font-size: 50px; line-height: 74px;
    padding-left: 40px; text-transform: uppercase; letter-spacing: .5px;
  }
  .contact {
    left: 0; top: 1008px; width: 790px; height: 72px;
    background: linear-gradient(180deg, #f2f2f2, #cfcfcf);
    display: flex; align-items: center; gap: 24px; padding-left: 36px;
    font-family: "Roboto", sans-serif; font-weight: 700; font-size: 17px;
    color: var(--ink-dark); text-transform: uppercase;
  }
  .contact .item { display: flex; align-items: center; gap: 8px; }
  .base-band { left: 0; top: 1080px; width: 790px; height: 20px; background: var(--blue); }
</style>
</head>
<body>
  <main class="flyer">
    <div class="abs hero-photo" role="img" aria-label="Photo of a modern open-plan living room and kitchen with downlights and a grey sofa"></div>
    <div class="abs web-strip"><span>www.torvinelectrics.com.au</span></div>
    <div class="abs brand">
      <div class="brand-dot"></div>
      <div class="brand-name">Torvin Electrics</div>
    </div>
    <div class="abs specialising">
      <div class="lead">Specialising in new homes,</div>
      <div class="sub">Renovations and commercial projects</div>
    </div>

    <div class="abs deals-label"><span>Specials Deals:</span></div>
    <div class="abs deals">
      <div class="big">10% Off</div>
      <div class="small">All electrical services</div>
      <div class="or">OR</div>
      <div class="big">Free LED</div>
      <div class="small">Downlights on installation</div>
    </div>
    <div class="abs kitchen-photo" role="img" aria-label="Photo of a kitchen with pendant lights, ovens and bar stools"></div>

    <div class="abs services-title">
      <div class="l1">All residential</div>
      <div class="l2">and commercial</div>
      <div class="l3">Electrical services</div>
    </div>
    <div class="abs services-list">
      <ul>
        <li>New Home Installations</li>
        <li>Commercial projects</li>
        <li>Shop fit outs</li>
        <li>Renovations</li>
        <li>Smoke Detectors</li>
        <li>Air Conditioning and Ceiling Fans</li>
        <li>Garden Lighting</li>
        <li>Oven and Cooktop Installations</li>
      </ul>
      <ul>
        <li>Power Point installation</li>
        <li>LED lighting upgrades</li>
        <li>Security Lighting</li>
        <li>Switchboard upgrades</li>
        <li>Test and Tag</li>
        <li>Commercial Property</li>
        <li>General Electrical Maintenance</li>
      </ul>
    </div>

    <div class="abs call">Call us today: 0457 613 948</div>
    <div class="abs contact">
      <div class="item">
        <svg width="18" height="13" viewBox="0 0 18 13" aria-hidden="true">
          <rect x="1" y="1" width="16" height="11" fill="none" stroke="#1b1b1b" stroke-width="1.5"/>
          <path d="M1 1 L9 7 L17 1 M1 12 L7 6 M17 12 L11 6" fill="none" stroke="#1b1b1b" stroke-width="1.2"/>
        </svg>
        <span>admin@torvinelectrics.com.au</span>
      </div>
      <div class="item"><span>www.facebook.com/TorvinElectrics</span></div>
    </div>
    <div class="abs base-band"></div>
  </main>
</body>
</html>
```